International Website Security StartUp needs a banner ads design

We need an advertisement of our product and company "GuardNestly" that we can use in blogs and communities around WordPress.
We want the ad to communicate that you need a website security solution and that if you are looking for one, ours is the best on the market.
The ad should use our basic colors (white, red, black, grey) or shades/variations of this. It should not look to dark, but friendly and helpful. No animation please.
I need a banner design for display advertising campaign. Sizes needed are as follows:
234x60
160 x 600
125x125
250 x 250
300 x 250
468 x 60
728 x 90
Our product is a website security suite which comes in four editions. Pricing starts at $10/month.
Our solution helps basically every website owner to protect his website/blog/online business against hackers and malware attacks.
Other then other solutions we have an AI engine which even can find never before seen malware and finds around 40% more malware then signature based approaches. These AI engine was even funded by the Federal research council of Verdania as one of the upcoming and outstanding technologies to make the internet safer.
Our solution (depending on the edition) includes Blacklist and reputation Monitoring, Speed & Uptime Monitoring for the website, Standard and Advanced Malware Monitoring. We also offer Vulnerability Assessments and Facebook Wall Protection within the packages. Best of all is that we have an automated malware cleanup included in the product, so that also not technical people can use our software and their site is cleaned from malware automatically even if they don't know how to do that, as we do it for them. Fully automated the moment malware is discovered on the page, without submitting a support ticket and waiting for feedback.
The scan frequency of our product varies from weekly to continuously.
To read more about our product and company have a look at www.guardnestly-example.com.
Target Market(s)
WordPress Users, Designer & WebAgencies looking for a website security solution
Industry/Entity Type
Advertising

```html
<!DOCTYPE html>
<html lang="en">
<head>
<meta charset="utf-8">
<title>GuardNestly – Display Banner Set</title>
<link href="https://fonts.googleapis.com/css2?family=PT+Sans+Narrow:wght@400&display=swap" rel="stylesheet">
<style>
  :root {
    --teal-deep: #1e7c93;
    --teal-bright: #42d8e2;
    --teal-low: #2a9db0;
    --panel-dark: #2b2b2b;
    --panel-mid: #4a4a4a;
    --silver-light: #f4f4f4;
    --silver-mid: #c9c9c9;
    --silver-dark: #8f8f8f;
    --frame: #ffffff;
    --ink: #222222;
    --accent: #e3003b;
    --accent-edge: #5a0a1a;
    --text-light: #ffffff;
  }
  * { box-sizing: border-box; margin: 0; padding: 0; }
  html, body { width: 1200px; height: 840px; overflow: hidden; }
  body {
    position: relative;
    font-family: "PT Sans Narrow", "Arial Narrow", sans-serif;
    background: linear-gradient(180deg, var(--teal-deep) 0%, var(--teal-bright) 47%, var(--teal-low) 100%);
  }
  .banner {
    position: absolute;
    border: 3px solid var(--frame);
    background: radial-gradient(ellipse at 50% 45%, var(--panel-mid) 0%, var(--panel-dark) 100%);
    overflow: hidden;
  }
  .banner__header { position: absolute; left: 0; top: 0; }
  .brand-dot {
    position: absolute;
    border-radius: 50%;
    background: var(--accent);
    border: 4px solid var(--panel-dark);
  }
  .brand-name {
    position: absolute;
    color: var(--ink);
    font-weight: 400;
    white-space: nowrap;
    line-height: 1;
  }
  .headline {
    position: absolute;
    color: var(--text-light);
    text-align: center;
  }
  .cta {
    position: absolute;
    display: flex;
    align-items: center;
    justify-content: center;
    background: var(--accent);
    border: 1px solid var(--accent-edge);
    color: var(--text-light);
    font-size: 18px;
    white-space: nowrap;
  }

  /* 160 x 600 skyscraper */
  .banner--skyscraper { left: 40px; top: 95px; width: 192px; height: 720px; }
  .banner--skyscraper .brand-dot { left: 46px; top: 14px; width: 100px; height: 100px; }
  .banner--skyscraper .brand-name { left: 0; width: 186px; text-align: center; top: 118px; font-size: 25px; }
  .banner--skyscraper .headline { left: 0; width: 186px; top: 240px; font-size: 36px; line-height: 58px; }
  .banner--skyscraper .cta { left: 7px; top: 655px; width: 174px; height: 40px; }

  /* 300 x 250 rectangle */
  .banner--rectangle { left: 406px; top: 304px; width: 360px; height: 300px; }
  .banner--rectangle .brand-dot { left: 44px; top: 8px; width: 76px; height: 76px; }
  .banner--rectangle .brand-name { left: 132px; top: 33px; font-size: 26px; }
  .banner--rectangle .headline { left: 0; width: 354px; top: 134px; font-size: 29px; line-height: 44px; }
  .banner--rectangle .cta { left: 97px; top: 239px; width: 174px; height: 40px; }

  /* 728 x 90 leaderboard */
  .banner--leaderboard { left: 241px; top: 676px; width: 874px; height: 109px; }
  .banner--leaderboard .brand-dot { left: 61px; top: 0px; width: 76px; height: 76px; }
  .banner--leaderboard .brand-name { left: 0; width: 204px; text-align: center; top: 80px; font-size: 24px; }
  .banner--leaderboard .headline { left: 240px; width: 400px; top: 8px; font-size: 36px; line-height: 45px; }
  .banner--leaderboard .cta { left: 677px; top: 33px; width: 172px; height: 40px; }
</style>
</head>
<body>

  <!-- 160 x 600 -->
  <section class="banner banner--skyscraper" aria-label="GuardNestly skyscraper banner">
    <svg class="banner__header" width="186" height="190" viewBox="0 0 186 190">
      <defs>
        <linearGradient id="silverSky" x1="0" y1="0" x2="1" y2="0">
          <stop offset="0" stop-color="var(--silver-dark)"/>
          <stop offset="0.5" stop-color="var(--silver-light)"/>
          <stop offset="1" stop-color="var(--silver-mid)"/>
        </linearGradient>
      </defs>
      <path d="M0 0H186V160Q95 150 0 178Z" fill="var(--frame)"/>
      <path d="M0 0H186V150Q95 138 0 150Z" fill="url(#silverSky)"/>
    </svg>
    <span class="brand-dot"></span>
    <span class="brand-name">GuardNestly</span>
    <p class="headline">Website<br>malware<br>monitoring<br>&amp; automated<br>cleanup</p>
    <span class="cta">Protect your business</span>
  </section>

  <!-- 300 x 250 -->
  <section class="banner banner--rectangle" aria-label="GuardNestly rectangle banner">
    <svg class="banner__header" width="354" height="110" viewBox="0 0 354 110">
      <defs>
        <linearGradient id="silverRect" x1="0" y1="0" x2="1" y2="0">
          <stop offset="0" stop-color="var(--silver-dark)"/>
          <stop offset="0.55" stop-color="var(--silver-light)"/>
          <stop offset="1" stop-color="var(--silver-mid)"/>
        </linearGradient>
      </defs>
      <path d="M0 0H354V84Q180 78 0 100Z" fill="var(--frame)"/>
      <path d="M0 0H354V75Q180 66 0 78Z" fill="url(#silverRect)"/>
    </svg>
    <span class="brand-dot"></span>
    <span class="brand-name">GuardNestly</span>
    <p class="headline">Website malware monitoring<br>&amp; automated cleanup</p>
    <span class="cta">Protect your business</span>
  </section>

  <!-- 728 x 90 -->
  <section class="banner banner--leaderboard" aria-label="GuardNestly leaderboard banner">
    <svg class="banner__header" width="220" height="103" viewBox="0 0 220 103">
      <defs>
        <linearGradient id="silverLead" x1="0" y1="0" x2="1" y2="0">
          <stop offset="0" stop-color="var(--silver-dark)"/>
          <stop offset="0.5" stop-color="var(--silver-light)"/>
          <stop offset="1" stop-color="var(--silver-mid)"/>
        </linearGradient>
      </defs>
      <path d="M0 0H210Q198 50 218 103H0Z" fill="var(--frame)"/>
      <path d="M0 0H200Q188 50 206 103H0Z" fill="url(#silverLead)"/>
    </svg>
    <span class="brand-dot"></span>
    <span class="brand-name">GuardNestly</span>
    <p class="headline">Website malware monitoring<br>&amp; automated cleanup</p>
    <span class="cta">Protect your business</span>
  </section>

</body>
</html>
```